Webbanner-Design für Informatik Dienstleistungen und Webdesign
Zielgruppe
Informatik Dienstleistungen und Webdesign
Aufgabenstellung
Es soll immer das gleiche Gesicht auf den Banner und ein kurzer Satz.
1. Sie haben das Business - wir die Software
2. Sie haben Anforderungen - wir Lösungen
3. Sie brauchen Unterstützung - wir helfen
Die Banner sollen auf unserer Homepage www.varmek-design.ch auf der Startseite durchlaufen. Das Format soll 1200x500 Pixel sein

```html
<!DOCTYPE html>
<html lang="de">
<head>
<meta charset="utf-8">
<title>Sie haben das Business – wir die Software</title>
<link rel="stylesheet" href="https://fonts.googleapis.com/css2?family=Arimo:ital,wght@1,400;1,700&display=swap">
<style>
  :root {
    --navy: #0c2a42;
    --navy-light: #163a56;
    --sky: #0a7fc8;
    --photo-warm: #b79a82;
    --photo-dark: #2a2a2e;
    --white: #ffffff;
    --ink: #0c2a42;
  }
  * { margin: 0; padding: 0; box-sizing: border-box; }
  html, body { width: 1200px; height: 500px; overflow: hidden; background: var(--navy); }
  .banner {
    position: relative;
    width: 1200px;
    height: 500px;
    overflow: hidden;
    font-family: "Arimo", Arial, sans-serif;
  }
  .banner__backdrop {
    position: absolute;
    inset: 0;
    background: radial-gradient(ellipse at 30% 45%, var(--navy-light) 0%, var(--navy) 70%);
  }
  .banner__shapes {
    position: absolute;
    inset: 0;
  }
  .banner__portrait {
    position: absolute;
    left: 650px;
    top: 0;
    width: 550px;
    height: 500px;
    clip-path: polygon(34% 0, 100% 0, 100% 100%, 0 100%, 6% 70%, 18% 35%);
    background: linear-gradient(160deg, var(--photo-warm) 0%, #8f7562 45%, var(--photo-dark) 100%);
    opacity: 0.85;
  }
  .headline {
    position: absolute;
    left: 30px;
    top: 183px;
    color: var(--white);
    font-style: italic;
  }
  .headline__lead {
    display: block;
    font-size: 46px;
    line-height: 60px;
    letter-spacing: 0.5px;
  }
  .headline__lead strong { font-weight: 700; }
  .headline__lead span { font-weight: 400; }
  .headline__answer {
    display: inline-block;
    margin-top: 4px;
    margin-left: 3px;
    width: 457px;
    height: 64px;
    padding-left: 22px;
    background: var(--white);
    color: var(--ink);
    font-size: 44px;
    font-weight: 700;
    line-height: 64px;
    letter-spacing: 0.5px;
  }
  .headline__dot {
    position: absolute;
    left: 470px;
    top: 88px;
    font-size: 44px;
    font-weight: 700;
    line-height: 64px;
    color: var(--white);
  }
</style>
</head>
<body>
<main class="banner">
  <div class="banner__backdrop" role="img" aria-label="Gedämpftes Hintergrundfoto mit Skizzen von Webseiten-Layouts auf Papier"></div>

  <svg class="banner__shapes" width="1200" height="500" viewBox="0 0 1200 500" aria-hidden="true">
    <polygon points="812,0 1200,0 1200,500 556,500" fill="var(--sky)"/>
  </svg>

  <div class="banner__portrait" role="img" aria-label="Porträtfoto einer lächelnden jungen Frau mit langen blonden Haaren in dunklem Oberteil"></div>

  <h1 class="headline">
    <span class="headline__lead"><span>Sie haben </span><strong>das Business</strong></span>
    <span class="headline__answer">wir die Software</span>
    <span class="headline__dot">.</span>
  </h1>
</main>
</body>
</html>
```